Increased budget: GUI redesign: 10 year old user interface needs modern look-and-feel

UPDATE: Please DO look at more than only th eone image I attached! Almost all designs are simply reworks of that one picture. That is not what we are looking for. Check out the video to understand what the product does, and try to make something better.
We have an existing app (see https://www.vextorane.com/downloadBrivoPanel.php?vers=3_9_1_140964&dir=Vextorane_OEM/3_9_1_140964&name=DSP_Control_Software) which needs refreshing. See also a video here: https://vextorane-oem.com/software/ and the user manual attached here. The GUI is now 800x400 pixels, which is too small; and not scalable, which will be fixed in the future. We need a new, modern look-and-feel, and images that can be exported from the design in various sizes. The current design is attached as well as a collection of PNG files. The overall layout can stay similar, although we are open to good ideas for improvements. The design should be targeted at professional users, not end users; the product is used by audio professionals (e.g. sound engineers, loudspeaker designers). Also see our web version: https://www.vextorane.com/brivopanel/skins/1_1_2/container.html?MAC=Demo%201x2
The winner will also be asked to do a full design of the application GUI (based on the design done here), with several more windows etc, and additional payment depending on the work to be done.

Target Market(s)

Professional audio

Industry/Entity Type

Audio / Industrial

Font styles to use
Other font styles liked:
• Futura (not mandatory)

Colors

Designer to choose colors to be used in the design.

Requirements
Must have
• Modern, timeless design, not too bling bling
Nice to have
• Flat design
Should not have
• 3D, bling bling, many colours, etc

```html
<!DOCTYPE html>
<html lang="en">
<head>
<meta charset="utf-8">
<title>Vextorane DSP Control – Input 1</title>
<link href="https://fonts.googleapis.com/css2?family=Jost:wght@400;500;600&display=swap" rel="stylesheet">
<style>
:root{
  --bg:#1f1f1f;
  --shell:#262626;
  --panel:#2b2b2b;
  --sidebar:#151515;
  --btn:#1c1c1c;
  --field:#3a3a3a;
  --field-border:#4a4a4a;
  --select:#050505;
  --plot:#000;
  --grid:#4d4d4d;
  --text:#e8e8e8;
  --muted:#c9c9c9;
  --accent:#f28a0c;
  --accent-dark:#e07800;
  --green:#39d12a;
  --logo:#0f2a3a;
}
*{box-sizing:border-box;margin:0;padding:0}
html,body{width:1200px;height:1200px;overflow:hidden;background:var(--bg)}
body{font-family:'Jost',sans-serif;color:var(--text);position:relative}
.abs{position:absolute}
.shell{left:60px;top:310px;width:1080px;height:579px;background:var(--shell);border-radius:12px}
.sidebar{left:70px;top:320px;width:139px;height:559px;background:var(--sidebar);border-radius:8px}
.workspace{left:214px;top:320px;width:915px;height:559px;background:var(--panel);border-radius:8px}
.brand{left:112px;top:340px;width:56px;height:56px;background:var(--logo);display:flex;align-items:center;justify-content:center;font-size:12px;font-weight:500;color:#fff;letter-spacing:.3px}
.nav-btn{left:80px;width:119px;height:28px;background:var(--btn);border-radius:3px;font-size:8px;display:flex;align-items:center;justify-content:center;color:#f0f0f0;box-shadow:0 2px 3px rgba(0,0,0,.4)}
.nav-btn.active{background:var(--accent);font-weight:600;color:#fff}
.graph{left:229px;top:335px;width:759px;height:260px;background:var(--plot);border-radius:8px}
.axis-label{font-size:9.5px;color:#d8d8d8;transform:translate(-50%,-50%)}
.col-head{font-size:12px;font-weight:600;color:#e0e0e0;transform:translate(-50%,-50%);top:618px}
.led{width:20px;height:20px;border-radius:50%;background:radial-gradient(circle,#3a3a3a 0,#252525 70%);border:1px solid #3c3c3c;transform:translate(-50%,-50%)}
.led::after{content:"";position:absolute;left:8px;top:8px;width:2px;height:2px;border-radius:50%;background:#555}
.led.on{background:radial-gradient(circle,#8fe05a 0,#3b7a22 35%,#252525 75%)}
.led.on::after{background:#dfffcf}
.led.red{background:radial-gradient(circle,#ff6b6b 0,#8c1d1d 40%,#252525 75%)}
.led.red::after{background:#ffd0d0}
.select{height:27px;background:var(--select);border-radius:3px;font-size:8px;display:flex;align-items:center;padding-left:7px;transform:translateY(-50%)}
.select::after{content:"";position:absolute;right:7px;top:10px;border-left:3.5px solid transparent;border-right:3.5px solid transparent;border-top:6px solid #fff}
.field{height:27px;background:var(--field);border:1px solid var(--field-border);border-radius:3px;font-size:8px;display:flex;align-items:center;justify-content:center;transform:translateY(-50%)}
.section-label{font-size:12px;font-weight:600;color:#e0e0e0;transform:translateY(-50%)}
.mute{left:902px;top:649px;width:82px;height:36px;background:#2f2f2f;border-radius:4px;font-size:9px;box-shadow:0 2px 4px rgba(0,0,0,.35)}
.fx-title{font-size:11.5px;color:#e4e4e4;top:708px}
.fx-rule{height:1px;background:#8a8a8a;top:722px}
.badge{left:1063px;top:709px;width:46px;height:10px;background:#555;border-radius:2px;font-size:6.5px;display:flex;align-items:center;justify-content:center;color:#eee}
.value-box{top:792px;height:20px;background:#353535;border:1px solid #4c4c4c;border-radius:3px;font-size:8px;display:flex;align-items:center;justify-content:center}
.knob-label{top:825px;font-size:11px;font-weight:600;color:#dedede;transform:translate(-50%,-50%)}
.meter-num{font-size:9px;color:#dcdcdc;transform:translateY(-50%)}
.scale-ticks{width:7px;height:254px;top:338px;background:repeating-linear-gradient(to bottom,#8a8a8a 0 1px,transparent 1px 4.2px)}
.meter{left:1068px;top:336px;width:8px;height:258px;background:
  repeating-linear-gradient(to bottom,transparent 0 2.9px,#000 2.9px 4.2px),
  linear-gradient(to bottom,#5a1616 0,#5a1616 8%,#6b5a12 8%,#6b5a12 22%,#1f5a1a 22%,#1f5a1a 32%,var(--green) 32%,var(--green) 100%)}
.db-box{left:1008px;top:604px;width:64px;height:20px;background:#2a2a2a;border:1px solid #4c4c4c;border-radius:3px;font-size:8px;display:flex;align-items:center;justify-content:center}
</style>
</head>
<body>
<div class="abs shell"></div>
<div class="abs sidebar"></div>
<div class="abs workspace"></div>

<div class="abs brand">VEXTORANE</div>

<div class="abs nav-btn" style="top:421px">Main</div>
<div class="abs nav-btn" style="top:465px">X-over</div>
<div class="abs nav-btn active" style="top:509px">In 1</div>
<div class="abs nav-btn" style="top:553px">In 2</div>
<div class="abs nav-btn" style="top:596px">In 3</div>
<div class="abs nav-btn" style="top:640px">In 4</div>
<div class="abs nav-btn" style="top:684px">Out 1</div>
<div class="abs nav-btn" style="top:728px">Out 2</div>
<div class="abs nav-btn" style="top:772px">Out 3</div>
<div class="abs nav-btn" style="top:815px">Out 4</div>

<!-- EQ graph -->
<div class="abs graph"></div>
<svg class="abs" style="left:0;top:0" width="1200" height="1200" aria-label="EQ response graph">
  <g fill="none" stroke="#bdbdbd" stroke-width="0.9">
    <rect x="244" y="349" width="13" height="13" rx="2"/>
    <path d="M247 352l7 7M247 352h3M247 352v3M254 359h-3M254 359v-3"/>
    <rect x="244" y="373" width="13" height="13" rx="2"/>
    <circle cx="250" cy="379" r="3"/><path d="M252.2 381.2l2.3 2.3"/>
    <rect x="244" y="397" width="13" height="13" rx="2"/>
    <path d="M247.5 400.5h6M250.5 400.5v7"/>
  </g>
  <g stroke="var(--grid)" stroke-width="0.8" fill="none">
    <rect x="270" y="351" width="673" height="208"/>
    <line x1="337" y1="351" x2="337" y2="559"/><line x1="404" y1="351" x2="404" y2="559"/>
    <line x1="472" y1="351" x2="472" y2="559"/><line x1="539" y1="351" x2="539" y2="559"/>
    <line x1="606" y1="351" x2="606" y2="559"/><line x1="673" y1="351" x2="673" y2="559"/>
    <line x1="741" y1="351" x2="741" y2="559"/><line x1="808" y1="351" x2="808" y2="559"/>
    <line x1="875" y1="351" x2="875" y2="559"/>
    <line x1="270" y1="403" x2="943" y2="403"/><line x1="270" y1="507" x2="943" y2="507"/>
  </g>
  <line x1="270" y1="455" x2="943" y2="455" stroke="#cfcfcf" stroke-width="1"/>
  <g font-family="Jost, sans-serif" font-size="7" fill="#fff" text-anchor="middle" stroke="#fff" stroke-width="0.6">
    <circle cx="336" cy="455" r="7.5" fill="#b3121c"/>
    <circle cx="401" cy="455" r="7.5" fill="#a8650c"/>
    <circle cx="467" cy="455" r="7.5" fill="#a6a10c"/>
    <circle cx="532" cy="455" r="7.5" fill="#1a9a1a"/>
    <circle cx="598" cy="455" r="7.5" fill="#11a3a3"/>
    <circle cx="664" cy="455" r="7.5" fill="#0c12b0"/>
    <circle cx="729" cy="455" r="7.5" fill="#b010b0"/>
    <circle cx="795" cy="455" r="7.5" fill="#b3320f"/>
    <circle cx="860" cy="455" r="7.5" fill="#a8990c"/>
    <circle cx="926" cy="455" r="7.5" fill="#1bbf1b"/>
  </g>
  <g font-family="Jost, sans-serif" font-size="7" fill="#fff" text-anchor="middle">
    <text x="336" y="457.5">1</text><text x="401" y="457.5">2</text><text x="467" y="457.5">3</text>
    <text x="532" y="457.5">4</text><text x="598" y="457.5">5</text><text x="664" y="457.5">6</text>
    <text x="729" y="457.5">7</text><text x="795" y="457.5">8</text><text x="860" y="457.5">9</text>
    <text x="926" y="457.5">10</text>
  </g>

  <!-- knobs -->
  <g fill="none">
    <g transform="translate(933 759)">
      <circle r="28" stroke="#2e2e2e" stroke-width="4"/>
      <path d="M-19.8 19.8A28 28 0 0 1 0 -28" stroke="#8fdb2a" stroke-width="1.6" stroke-dasharray="1.2 2"/>
      <circle r="17" fill="#2a2a2a" stroke="#1a1a1a" stroke-width="3"/>
      <circle cy="-13" r="0.8" fill="#bbb"/>
    </g>
    <g transform="translate(1007 759)">
      <circle r="28" stroke="#2e2e2e" stroke-width="4"/>
      <path d="M-19.8 19.8A28 28 0 0 1 0 -28" stroke="#8fdb2a" stroke-width="1.6" stroke-dasharray="1.2 2"/>
      <circle r="17" fill="#2a2a2a" stroke="#1a1a1a" stroke-width="3"/>
      <circle cy="-13" r="0.8" fill="#bbb"/>
    </g>
    <g transform="translate(1076 759)">
      <circle r="28" stroke="#2e2e2e" stroke-width="4"/>
      <path d="M-19.8 19.8A28 28 0 0 1 0 -28" stroke="#8fdb2a" stroke-width="1.6" stroke-dasharray="1.2 2"/>
      <circle r="17" fill="#2a2a2a" stroke="#1a1a1a" stroke-width="3"/>
      <circle cy="-13" r="0.8" fill="#bbb"/>
    </g>
  </g>

  <!-- fader -->
  <rect x="1048" y="335" width="6" height="260" rx="3" fill="#111"/>
  <rect x="1041" y="385" width="20" height="43" rx="2" fill="#3a3a3a"/>
  <g stroke="#555" stroke-width="0.8">
    <line x1="1042" y1="392" x2="1060" y2="392"/><line x1="1042" y1="397" x2="1060" y2="397"/>
    <line x1="1042" y1="402" x2="1060" y2="402"/><line x1="1042" y1="412" x2="1060" y2="412"/>
    <line x1="1042" y1="417" x2="1060" y2="417"/><line x1="1042" y1="422" x2="1060" y2="422"/>
  </g>
  <line x1="1042" y1="407" x2="1060" y2="407" stroke="#ddd" stroke-width="0.8"/>
</svg>

<!-- graph axes -->
<div class="abs axis-label" style="left:959px;top:353px">15</div>
<div class="abs axis-label" style="left:959px;top:387px">10</div>
<div class="abs axis-label" style="left:957px;top:421px">5</div>
<div class="abs axis-label" style="left:964px;top:455px">0dB</div>
<div class="abs axis-label" style="left:960px;top:489px">- 5</div>
<div class="abs axis-label" style="left:963px;top:523px">- 10</div>
<div class="abs axis-label" style="left:963px;top:557px">- 15</div>
<div class="abs axis-label" style="left:249px;top:577px">10</div>
<div class="abs axis-label" style="left:316px;top:577px">20</div>
<div class="abs axis-label" style="left:384px;top:577px">50</div>
<div class="abs axis-label" style="left:454px;top:577px">100</div>
<div class="abs axis-label" style="left:527px;top:577px">200</div>
<div class="abs axis-label" style="left:601px;top:577px">500</div>
<div class="abs axis-label" style="left:671px;top:577px">1k</div>
<div class="abs axis-label" style="left:736px;top:577px">2k</div>
<div class="abs axis-label" style="left:803px;top:577px">5k</div>
<div class="abs axis-label" style="left:872px;top:577px">10k</div>
<div class="abs axis-label" style="left:943px;top:577px">20k</div>

<!-- EQ table headers -->
<div class="abs col-head" style="left:243px">On</div>
<div class="abs col-head" style="left:281px">Type</div>
<div class="abs col-head" style="left:373px">Freq</div>
<div class="abs col-head" style="left:448px">Q</div>
<div class="abs col-head" style="left:498px">Gain</div>
<div class="abs col-head" style="left:549px">On</div>
<div class="abs col-head" style="left:587px">Type</div>
<div class="abs col-head" style="left:679px">Freq</div>
<div class="abs col-head" style="left:754px">Q</div>
<div class="abs col-head" style="left:804px">Gain</div>

<!-- EQ bands, left group -->
<div class="abs led on" style="left:243px;top:645px"></div>
<div class="abs select" style="left:262px;top:645px;width:86px">Bell</div>
<div class="abs field" style="left:355px;top:645px;width:65px">20Hz</div>
<div class="abs field" style="left:426px;top:645px;width:44px">1</div>
<div class="abs field" style="left:476px;top:645px;width:44px">0dB</div>

<div class="abs led" style="left:243px;top:679px"></div>
<div class="abs select" style="left:262px;top:679px;width:86px">Notch</div>
<div class="abs field" style="left:355px;top:679px;width:65px">20Hz</div>
<div class="abs field" style="left:426px;top:679px;width:44px">1</div>
<div class="abs field" style="left:476px;top:679px;width:44px">0dB</div>

<div class="abs led" style="left:243px;top:712px"></div>
<div class="abs select" style="left:262px;top:712px;width:86px">AllPass</div>
<div class="abs field" style="left:355px;top:712px;width:65px">20Hz</div>
<div class="abs field" style="left:426px;top:712px;width:44px">1</div>
<div class="abs field" style="left:476px;top:712px;width:44px">0dB</div>

<div class="abs led" style="left:243px;top:746px"></div>
<div class="abs select" style="left:262px;top:746px;width:86px">Low Shelf</div>
<div class="abs field" style="left:355px;top:746px;width:65px">20Hz</div>
<div class="abs field" style="left:426px;top:746px;width:44px">1</div>
<div class="abs field" style="left:476px;top:746px;width:44px">0dB</div>

<div class="abs led" style="left:243px;top:780px"></div>
<div class="abs select" style="left:262px;top:780px;width:86px">Band Pass</div>
<div class="abs field" style="left:355px;top:780px;width:65px">20Hz</div>
<div class="abs field" style="left:426px;top:780px;width:44px">1</div>
<div class="abs field" style="left:476px;top:780px;width:44px">0dB</div>

<!-- EQ bands, right group -->
<div class="abs led on" style="left:549px;top:645px"></div>
<div class="abs select" style="left:568px;top:645px;width:86px">Bell</div>
<div class="abs field" style="left:661px;top:645px;width:65px">20Hz</div>
<div class="abs field" style="left:732px;top:645px;width:44px">1</div>
<div class="abs field" style="left:782px;top:645px;width:44px">0dB</div>

<div class="abs led" style="left:549px;top:679px"></div>
<div class="abs select" style="left:568px;top:679px;width:86px">Notch</div>
<div class="abs field" style="left:661px;top:679px;width:65px">20Hz</div>
<div class="abs field" style="left:732px;top:679px;width:44px">1</div>
<div class="abs field" style="left:782px;top:679px;width:44px">0dB</div>

<div class="abs led" style="left:549px;top:712px"></div>
<div class="abs select" style="left:568px;top:712px;width:86px">AllPass</div>
<div class="abs field" style="left:661px;top:712px;width:65px">20Hz</div>
<div class="abs field" style="left:732px;top:712px;width:44px">1</div>
<div class="abs field" style="left:782px;top:712px;width:44px">0dB</div>

<div class="abs led" style="left:549px;top:746px"></div>
<div class="abs select" style="left:568px;top:746px;width:86px">Low Shelf</div>
<div class="abs field" style="left:661px;top:746px;width:65px">20Hz</div>
<div class="abs field" style="left:732px;top:746px;width:44px">1</div>
<div class="abs field" style="left:782px;top:746px;width:44px">0dB</div>

<div class="abs led" style="left:549px;top:780px"></div>
<div class="abs select" style="left:568px;top:780px;width:86px">Band Pass</div>
<div class="abs field" style="left:661px;top:780px;width:65px">20Hz</div>
<div class="abs field" style="left:732px;top:780px;width:44px">1</div>
<div class="abs field" style="left:782px;top:780px;width:44px">0dB</div>

<!-- filters -->
<div class="abs section-label" style="left:245px;top:817px">HPF</div>
<div class="abs led" style="left:243px;top:841px"></div>
<div class="abs field" style="left:262px;top:841px;width:82px">Off</div>
<div class="abs select" style="left:350px;top:841px;width:170px">Butterworth 6dB</div>

<div class="abs section-label" style="left:551px;top:817px">LPF</div>
<div class="abs led" style="left:549px;top:841px"></div>
<div class="abs field" style="left:568px;top:841px;width:82px">Off</div>
<div class="abs select" style="left:656px;top:841px;width:170px">Butterworth 6dB</div>

<!-- level meter and fader scale -->
<div class="abs meter-num" style="left:1003px;top:338px;width:22px;text-align:right">+12</div>
<div class="abs meter-num" style="left:1003px;top:364px;width:22px;text-align:right">+6</div>
<div class="abs meter-num" style="left:1003px;top:389px;width:22px;text-align:right">0</div>
<div class="abs meter-num" style="left:1003px;top:415px;width:22px;text-align:right">-6</div>
<div class="abs meter-num" style="left:1003px;top:440px;width:22px;text-align:right">-12</div>
<div class="abs meter-num" style="left:1003px;top:465px;width:22px;text-align:right">-18</div>
<div class="abs meter-num" style="left:1003px;top:491px;width:22px;text-align:right">-24</div>
<div class="abs meter-num" style="left:1003px;top:516px;width:22px;text-align:right">-30</div>
<div class="abs meter-num" style="left:1003px;top:541px;width:22px;text-align:right">-36</div>
<div class="abs meter-num" style="left:1003px;top:567px;width:22px;text-align:right">-42</div>
<div class="abs meter-num" style="left:1003px;top:592px;width:22px;text-align:right">-48</div>
<div class="abs scale-ticks" style="left:1030px"></div>
<div class="abs scale-ticks" style="left:1037px;width:2px"></div>

<div class="abs meter"></div>
<div class="abs scale-ticks" style="left:1078px;width:2px"></div>
<div class="abs scale-ticks" style="left:1081px"></div>
<div class="abs meter-num" style="left:1094px;top:338px">+12</div>
<div class="abs meter-num" style="left:1094px;top:364px">+6</div>
<div class="abs meter-num" style="left:1094px;top:389px">0</div>
<div class="abs meter-num" style="left:1094px;top:415px">-6</div>
<div class="abs meter-num" style="left:1094px;top:440px">-12</div>
<div class="abs meter-num" style="left:1094px;top:465px">-18</div>
<div class="abs meter-num" style="left:1094px;top:491px">-24</div>
<div class="abs meter-num" style="left:1094px;top:516px">-30</div>
<div class="abs meter-num" style="left:1094px;top:541px">-36</div>
<div class="abs meter-num" style="left:1094px;top:567px">-42</div>
<div class="abs meter-num" style="left:1094px;top:592px">-48</div>
<div class="abs db-box">0.00 dB</div>

<!-- mute -->
<div class="abs mute"></div>
<div class="abs" style="left:917px;top:661px;font-size:9px">Mute</div>
<div class="abs led red" style="left:959px;top:667px"></div>

<!-- delay / limiter -->
<div class="abs fx-title" style="left:902px">Delay</div>
<div class="abs fx-rule" style="left:902px;width:64px"></div>
<div class="abs fx-title" style="left:975px">Limiter</div>
<div class="abs fx-rule" style="left:975px;width:134px"></div>
<div class="abs badge">Compressor</div>

<div class="abs value-box" style="left:902px;width:64px">0.00 ms</div>
<div class="abs value-box" style="left:975px;width:64px">12 dBu</div>
<div class="abs value-box" style="left:1044px;width:65px">50 dB/s</div>
<div class="abs select" style="left:902px;top:828px;width:64px;height:19px;font-size:7px">ms</div>
<div class="abs knob-label" style="left:1007px">THR</div>
<div class="abs knob-label" style="left:1076px">REL</div>
</body>
</html>
```